Small business updating business cards

We have already updated our logo via Pixel Forum and downloaded it (hopefully) for you to use. Now an updated set of business cards for Neil Pollard and Stuart Pollard are also needed... we are also hoping that a copy of our outdated business card designs have uploaded successfully as Microsoft Publisher files. Our Strength Through Unity motto has died a slow death so we are hoping to remove it (and other superfluous lingo if the graphic covers the idea) and instead opt for a fancy graphic (?) on the second side of the card that really reflects our desire to obtain product / haulage from Road Transport / Yard Operators and convert legs of their haulage to rail freight where profitable (bulk haulage / containterised etc). Can you help us look larger, bolder and more robust than we really are (two man show)?
Target Market(s)
Transport Industry
Industry/Entity Type
Business
Contact Information for Business Card
Card details for both N Pollard and S Pollard have been uploaded on the publisher files
Colors
Designer to choose colors to be used in the design.
Requirements
Must have
- Similar theme both sides of card
Should not have
- Black on one side white on the other

```html
<!DOCTYPE html>
<html lang="en">
<head>
<meta charset="utf-8">
<title>Kestrail Business Cards</title>
<link rel="stylesheet" href="https://fonts.googleapis.com/css2?family=Open+Sans:wght@400;600;700;800&display=swap">
<style>
  :root {
    --bg: #eef0e6;
    --card: #ffffff;
    --teal: #0f8aa3;
    --teal-dark: #0b7f97;
    --cyan: #0aaee0;
    --gold: #9c8a3a;
    --ink-light: #ffffff;
    --shadow: rgba(0,0,0,0.18);
  }
  * { margin: 0; padding: 0; box-sizing: border-box; }
  html, body { width: 1200px; height: 835px; overflow: hidden; }
  body {
    background: var(--bg);
    font-family: "Open Sans", Arial, sans-serif;
    position: relative;
  }
  .card {
    position: absolute;
    top: 267px;
    width: 525px;
    height: 300px;
    background: var(--card);
    box-shadow: 0 10px 30px var(--shadow);
    overflow: hidden;
  }
  .card--front { left: 50px; }
  .card--back { left: 625px; }

  /* Front */
  .front-frame { position: absolute; inset: 0; }
  .front-name {
    position: absolute;
    inset: 0;
    display: flex;
    align-items: center;
    justify-content: center;
    font-weight: 800;
    font-size: 70px;
    color: var(--teal);
    letter-spacing: -1px;
  }

  /* Back */
  .back-logo {
    position: absolute;
    left: 40px;
    top: 38px;
    font-weight: 800;
    font-size: 30px;
    color: var(--teal);
    letter-spacing: -0.5px;
  }
  .back-tagline {
    position: absolute;
    right: 28px;
    top: 40px;
    width: 230px;
    font-weight: 700;
    font-size: 13px;
    line-height: 1.35;
    color: var(--teal);
    text-transform: uppercase;
  }
  .name-band {
    position: absolute;
    left: 0;
    top: 112px;
    width: 300px;
    height: 86px;
    background: var(--cyan);
    color: var(--ink-light);
    padding: 16px 0 0 32px;
  }
  .name-band__name {
    font-weight: 700;
    font-size: 27px;
    text-transform: uppercase;
    line-height: 1.1;
  }
  .name-band__role { font-size: 16px; line-height: 1.2; }
  .contact-panel {
    position: absolute;
    left: 300px;
    top: 100px;
    right: 0;
    bottom: 0;
    background: var(--teal-dark);
    color: var(--ink-light);
    padding: 26px 12px 0 18px;
    font-size: 12.5px;
    line-height: 1.45;
  }
  .contact-row { display: flex; gap: 9px; margin-bottom: 4px; }
  .contact-row svg { flex: none; width: 13px; height: 13px; margin-top: 3px; }
</style>
</head>
<body>

<section class="card card--front" aria-label="Card front">
  <svg class="front-frame" width="525" height="300" viewBox="0 0 525 300" fill="none" stroke="var(--gold)" stroke-width="1.5">
    <rect x="10" y="10" width="505" height="280"/>
    <rect x="16" y="16" width="493" height="268"/>
  </svg>
  <div class="front-name">Kestrail</div>
</section>

<section class="card card--back" aria-label="Card back">
  <div class="back-logo">Kestrail</div>
  <p class="back-tagline">Strategic alliance partner providing logistical freight solutions</p>

  <div class="name-band">
    <div class="name-band__name">Neil Pollard</div>
    <div class="name-band__role">Director</div>
  </div>

  <div class="contact-panel">
    <div class="contact-row">
      <svg viewBox="0 0 16 16" fill="none" stroke="currentColor" stroke-width="1.6"><path d="M4 1.5l2.5 3-1.5 2a8 8 0 0 0 4.5 4.5l2-1.5 3 2.5-1.5 2.5C7 14.5 1.5 9 1.5 3z"/></svg>
      <span>0412 738 260</span>
    </div>
    <div class="contact-row">
      <svg viewBox="0 0 16 16" fill="currentColor"><path d="M1 3h14v10H1z" opacity=".9"/><path d="M1 3l7 6 7-6" stroke="var(--teal-dark)" stroke-width="1.4" fill="none"/></svg>
      <span>pollardn@kestrail.com.au<br>kestrail@mailbox.com<br>kestrail@inbox.com</span>
    </div>
    <div class="contact-row">
      <svg viewBox="0 0 16 16" fill="none" stroke="currentColor" stroke-width="1.4"><circle cx="8" cy="8" r="6.5"/><path d="M1.5 8h13M8 1.5c3 3.5 3 9.5 0 13M8 1.5c-3 3.5-3 9.5 0 13"/></svg>
      <span>www.kestrail.com.au</span>
    </div>
    <div class="contact-row">
      <svg viewBox="0 0 16 16" fill="currentColor"><path d="M8 1a5 5 0 0 0-5 5c0 4 5 9 5 9s5-5 5-9a5 5 0 0 0-5-5zm0 7a2 2 0 1 1 0-4 2 2 0 0 1 0 4z"/></svg>
      <span>14 Ferndale Crescent Marlow<br>Park NSW 2290</span>
    </div>
  </div>
</section>

</body>
</html>
```